Faith Based Film Production Ecommerce Site Needed

We are a faith based film production company that offers coaching services as well as physical and digital products.

We have a Wordpress site on Hostwick. It currently, features a landing page (https://plumfernstudio.com/), however we now need a fully fleshed out interactive website that will feature short videos/trailers as well the ability for customers to make online purchases.

The updated site will feature 5 tabs - Take 1, Take 2, Take 3, BTS and Contact. This toolbar/menu should remain fixed/stable while visitors navigate the different tabs/pages, as shown here - https://dowgenbarsk.com/ (note this site is JUST a reference for its unmoving menu/toolbar in the top right corner of the page).

The text for each tab and actual video content will be provided for potential candidates. Until then, please improvise.

There will be 5 short trailers/reels featured under the "Take 2" tab, that will be shown as thumbnails the same size found here - https://dowgenbarsk.com/see-dowgen-at-work/ (reference for thumbnail size only). The names of these trailers will be called, Lantern Quest, Lantern Blooming, Lantern Dawn, Lantern Hearth, and Lantern Courtship.

Lastly, when arriving onto the page, visitors will be greeted with a inaudible video loop, similar to the one found here - https://www.tq-moviecraft.com/ (Note - this is a reference simply to show inaudible video looping). The ACTUAL video to be used however can be found here - https://clipvault.example/manage/videos/493817265, beginning at the 15 second mark when the 3 people are entering the cinema and ending at the 28 second mark where the screen gradually fades to black. The video will then consistently re-loop.

Once again, more detail will be provided for the most interesting submissions and of course, official winner.

Should you have any questions until then, please do not hesitate to reach out.

```html
<!DOCTYPE html>
<html lang="en">
<head>
<meta charset="utf-8">
<title>Plumfern Studio</title>
<link rel="stylesheet" href="https://fonts.googleapis.com/css2?family=Limelight&family=Kumbh+Sans:wght@400;600;700&display=swap">
<style>
:root{
  --gold:#d99a2b;
  --ink:#181818;
  --ink-deep:#121212;
  --ink-soft:#1e1e1e;
  --card:#1b1b1b;
  --white:#ffffff;
  --muted:#cfcfcf;
  --faint:#262626;
}
*{margin:0;padding:0;box-sizing:border-box}
html,body{width:1200px;height:3245px;overflow:hidden;background:var(--ink)}
body{position:relative;font-family:"Kumbh Sans",sans-serif;color:var(--white)}
.abs{position:absolute}
.display{font-family:"Limelight",serif;font-weight:400;letter-spacing:1px}

/* nav */
.site-nav{left:0;top:0;width:1200px;height:63px;background:#0f0f12;z-index:5}
.brand{left:164px;top:14px;font-weight:700;font-size:26px;letter-spacing:2px;display:flex;align-items:center;gap:8px}
.brand .dot{width:20px;height:20px;border:2px solid var(--white);border-radius:50%}
.menu{left:643px;top:22px;display:flex;gap:37px;font-size:13.5px}

/* hero */
.hero-media{left:0;top:63px;width:1200px;height:561px;background:radial-gradient(ellipse at 55% 55%,#3a3a66 0%,#1c2140 45%,#0c0f22 100%)}
.play{left:559px;top:586px;width:80px;height:80px;border:1.5px dashed var(--gold);border-radius:50%}
.play .core{position:absolute;left:8px;top:8px;width:62px;height:62px;border-radius:50%;background:var(--gold);border:3px solid #9b6a14}

.section-title{width:1200px;left:0;text-align:center;font-size:36px}
.section-title .accent{color:var(--gold)}
.rule{height:2px;background:var(--white)}
.vertical-word{font-family:"Limelight",serif;font-size:46px;color:var(--faint);transform:rotate(-90deg);transform-origin:left top;white-space:nowrap}

/* about */
.chair-art{left:239px;top:778px;width:176px;height:305px;background:linear-gradient(180deg,#f2f2f2 0%,#d8d8d8 70%,#2a2a2a 100%);border-radius:6px}
.about-copy{left:481px;top:806px;width:478px;font-size:12.6px;line-height:20.7px;text-align:justify;color:#e8e8e8}
.btn{background:var(--gold);color:var(--white);font-family:"Limelight",serif;font-size:11px;display:flex;align-items:center;justify-content:center;letter-spacing:.5px}

/* reels */
.reels-band{left:0;top:1133px;width:1200px;height:752px;background:var(--ink-soft);border-radius:50% 50% 0 0/70px 70px 0 0}
.reel{width:282px;height:207px;border-radius:50% 50% 0 0/16px 16px 0 0;overflow:visible}
.reel .thumb{position:absolute;inset:0;border-radius:inherit}
.reel .mini-play{position:absolute;left:124px;top:86px;width:34px;height:34px;border-radius:50%;background:rgba(40,40,40,.85)}
.reel .mini-play::after{content:"";position:absolute;left:13px;top:10px;border-left:11px solid var(--white);border-top:7px solid transparent;border-bottom:7px solid transparent}
.reel .label{position:absolute;left:58px;top:184px;width:166px;height:49px;background:var(--white);color:#111;border-radius:50% 50% 0 0/10px 10px 0 0;font-family:"Limelight",serif;font-size:11.5px;display:flex;align-items:center;justify-content:center}
.reel .label.featured{background:var(--gold);color:var(--white)}

/* services */
.services-band{left:0;top:1885px;width:1200px;height:458px;background:linear-gradient(180deg,#2f2b25 0%,#25221d 55%,#1e1c18 100%)}
.service{width:207px;height:237px;background:var(--card);text-align:center;padding-top:20px}
.service svg{display:block;margin:0 auto}
.service h3{font-family:"Limelight",serif;font-weight:400;font-size:11.5px;margin-top:14px;letter-spacing:.4px}
.service .bar{width:110px;height:1.5px;background:var(--white);margin:8px auto 14px}
.service p{font-size:11px;line-height:20px;color:#e4e4e4;padding:0 12px}

/* contact */
.contact-band{left:0;top:2343px;width:1200px;height:578px;background:var(--ink-deep)}
.field{background:var(--white);border-radius:3px;color:#9a9a9a;font-size:11.5px;padding:12px 13px}

/* footer */
.footer-band{left:0;top:2921px;width:1200px;height:324px;background:linear-gradient(180deg,#1a1816 0%,#22201d 60%,#1b1a18 100%)}
.footer-mark{left:282px;top:2993px;width:60px;height:79px;background:linear-gradient(180deg,#f0f0f0,#cfcfcf);border-radius:4px}
.footer-name{left:160px;top:3080px;width:304px;text-align:center;font-weight:700;font-size:22px;letter-spacing:2px}
.socials{left:237px;top:3113px;display:flex;gap:7px}
.socials span{width:28px;height:28px;border:1.5px solid var(--white);border-radius:50%}
.col-title{font-weight:600;font-size:15px}
.col-title::after{content:"";display:block;width:94px;height:2px;background:var(--white);margin-top:6px}
.col-list{list-style:none;font-size:12.5px;line-height:22px}
.info{font-size:12.5px;line-height:20px;display:flex;gap:10px}
.info svg{flex:none;margin-top:3px}
.footer-rule{left:149px;top:3160px;width:892px;height:1px;background:#8a8a8a}
.copyright{left:0;top:3184px;width:1200px;text-align:center;font-size:12px}
</style>
</head>
<body>

<header class="abs site-nav">
  <div class="abs brand"><span class="dot"></span>PLUMFERN STUDIO</div>
  <nav class="abs menu"><span>Home</span><span>Take 1</span><span>Take 2</span><span>Take 3</span><span>BTS</span><span>Contact</span></nav>
</header>

<div class="abs hero-media" role="img" aria-label="Looping video still: three friends eating popcorn in a dark cinema"></div>
<div class="abs play"><div class="core"><svg width="56" height="56" viewBox="0 0 56 56"><path d="M22 17 L38 28 L22 39Z" fill="#fff"/></svg></div></div>

<!-- about -->
<h2 class="abs section-title display" style="top:690px"><span class="accent">ABOUT</span> PLUMFERN STUDIO</h2>
<div class="abs rule" style="left:501px;top:744px;width:199px"></div>
<div class="abs vertical-word" style="left:1120px;top:1015px">ABOUT US</div>
<div class="abs chair-art" role="img" aria-label="Illustration of a white director's chair with candle flames"></div>
<p class="abs about-copy">Lorem ipsum dolor sit amet, consectetur adipiscing elit, sed do eiusmod tempor incididunt ut labore et dolore magna aliqua. Quis ipsum suspendisse ultrices gravida. Risus commodo viverra maecenas accumsan lacus vel facilisis. omnis iste natus error sit voluptatem accusantium doloremque laudantium, totam rem aperiam, eaque ipsa quae ab illo inventore veritatis et quasi architecto beatae vitae dicta sunt explicabo. Nemo enim ipsam voluptatem quia voluptas sit aspernatur aut odit aut fugit, sed quia consequuntur magni dolores eos qui ratione voluptatem sequi nesciunt. Neque porro quisquam est, qui dolorem ipsum quia dolor sit amet, consectetur, adipisci velit, sed quia non numquam eius modi tempora incidunt ut labore et dolore magnam.</p>
<div class="abs btn" style="left:481px;top:1027px;width:131px;height:38px">ABOUT US</div>

<!-- reels -->
<div class="abs reels-band"></div>
<h2 class="abs section-title display" style="top:1216px"><span class="accent">TAKE</span> 2</h2>
<div class="abs rule" style="left:550px;top:1271px;width:100px"></div>
<div class="abs vertical-word" style="left:40px;top:1600px">TAKE 2</div>

<div class="abs reel" style="left:162px;top:1299px"><div class="thumb" role="img" aria-label="Woman in an office looking at her phone" style="background:linear-gradient(135deg,#3a4658,#6b5a4a 55%,#1f2630)"></div><span class="mini-play"></span><div class="label">LANTERN QUEST</div></div>
<div class="abs reel" style="left:458px;top:1299px"><div class="thumb" role="img" aria-label="White orchid blossoms" style="background:linear-gradient(135deg,#f4f1e6,#d9d6b8 55%,#8da04a)"></div><span class="mini-play"></span><div class="label featured">LANTERN BLOOMING</div></div>
<div class="abs reel" style="left:754px;top:1299px"><div class="thumb" role="img" aria-label="Two hands clasped together" style="background:linear-gradient(135deg,#c9d3d6,#c89a7e 55%,#7b4c38)"></div><span class="mini-play"></span><div class="label">LANTERN DAWN</div></div>
<div class="abs reel" style="left:311px;top:1561px"><div class="thumb" role="img" aria-label="Bright living room with a blue sofa" style="background:linear-gradient(135deg,#dfe6ea,#b9c7cf 55%,#c8b79e)"></div><span class="mini-play"></span><div class="label">LANTERN HEARTH</div></div>
<div class="abs reel" style="left:607px;top:1561px"><div class="thumb" role="img" aria-label="Couple embracing by the sea at sunset" style="background:linear-gradient(135deg,#e3a65c,#a36b44 55%,#3a3a48)"></div><span class="mini-play"></span><div class="label">LANTERN COURTSHIP</div></div>

<!-- services -->
<div class="abs services-band" role="img" aria-label="Dim mountain landscape backdrop"></div>
<h2 class="abs section-title display" style="top:1950px"><span class="accent">WHAT</span> WE DO</h2>
<div class="abs rule" style="left:498px;top:2004px;width:204px"></div>
<div class="abs vertical-word" style="left:1120px;top:2280px">WHAT WE DO</div>

<div class="abs service" style="left:162px;top:2032px">
  <svg width="56" height="64" viewBox="0 0 56 64" fill="none" stroke="#fff" stroke-width="2"><rect x="6" y="8" width="36" height="50" rx="3"/><rect x="16" y="4" width="16" height="8" rx="2"/><path d="M12 24h6M22 24h14M12 34h6M22 34h14M12 44h6M22 44h14" /><circle cx="44" cy="20" r="8" stroke="#d99a2b"/><path d="M40 20l3 3 5-6" stroke="#d99a2b"/></svg>
  <h3>PROJECT DEVELOPMENT</h3><div class="bar"></div>
  <p>Lorem ipsum dolor sit amet, consectetur adipiscing elit, sed do eiusmod tempor incididunt ut labore et dolore magna.</p>
</div>
<div class="abs service" style="left:385px;top:2032px">
  <svg width="64" height="64" viewBox="0 0 64 64" fill="none" stroke="#d99a2b" stroke-width="2"><rect x="6" y="12" width="52" height="44" rx="2"/><path d="M6 12v44M14 12v44M22 24h26v22H22zM34 24v10h14"/><path d="M44 6l10 10-12 12-6-2 -2-6z"/></svg>
  <h3 style="color:var(--gold)">PRE-PRODUCTION</h3><div class="bar"></div>
  <p>Lorem ipsum dolor sit amet, consectetur adipiscing elit, sed do eiusmod tempor incididunt ut labore et dolore magna.</p>
</div>
<div class="abs service" style="left:608px;top:2032px">
  <svg width="66" height="64" viewBox="0 0 66 64" fill="none" stroke="#fff" stroke-width="2"><rect x="6" y="20" width="38" height="28"/><path d="M6 12l38-6 2 10-40 6z"/><path d="M14 10l4 10M24 8l4 10M34 7l4 10" stroke="#d99a2b"/><rect x="30" y="36" width="22" height="16" rx="2"/><path d="M52 40l8-4v16l-8-4"/><circle cx="36" cy="30" r="5" stroke="#d99a2b"/><circle cx="48" cy="30" r="5" stroke="#d99a2b"/></svg>
  <h3>PRODUCTION</h3><div class="bar"></div>
  <p>Lorem ipsum dolor sit amet, consectetur adipiscing elit, sed do eiusmod tempor incididunt ut labore et dolore magna.</p>
</div>
<div class="abs service" style="left:831px;top:2032px">
  <svg width="66" height="64" viewBox="0 0 66 64" fill="none" stroke="#fff" stroke-width="2"><rect x="4" y="6" width="58" height="26"/><path d="M4 12h58M4 26h58M14 6v26M52 6v26"/><path d="M28 14l8 5-8 5z" stroke="#d99a2b"/><path d="M22 32l20 18M44 32L24 50"/><circle cx="20" cy="54" r="6" stroke="#d99a2b"/><circle cx="46" cy="54" r="6" stroke="#d99a2b"/></svg>
  <h3>POST-PRODUCTION</h3><div class="bar"></div>
  <p>Lorem ipsum dolor sit amet, consectetur adipiscing elit, sed do eiusmod tempor incididunt ut labore et dolore magna.</p>
</div>

<!-- contact -->
<div class="abs contact-band"></div>
<h2 class="abs section-title display" style="top:2420px"><span class="accent">CONTACT</span> US</h2>
<div class="abs rule" style="left:550px;top:2474px;width:100px"></div>
<div class="abs field" style="left:219px;top:2518px;width:373px;height:38px">First Name</div>
<div class="abs field" style="left:608px;top:2518px;width:373px;height:38px">Last Name</div>
<div class="abs field" style="left:219px;top:2581px;width:373px;height:38px">Email Address</div>
<div class="abs field" style="left:608px;top:2581px;width:373px;height:38px">Phone Number</div>
<div class="abs field" style="left:219px;top:2643px;width:762px;height:128px">Message</div>
<div class="abs btn" style="left:535px;top:2808px;width:131px;height:36px">SUBMIT NOW</div>

<!-- footer -->
<footer>
  <div class="abs footer-band" role="img" aria-label="Dark landscape backdrop"></div>
  <div class="abs footer-mark" role="img" aria-label="Small director's chair illustration"></div>
  <div class="abs footer-name">PLUMFERN STUDIO</div>
  <div class="abs socials"><span></span><span></span><span></span><span></span></div>

  <div class="abs" style="left:490px;top:2978px">
    <div class="col-title">QUICK LINKS</div>
    <ul class="col-list" style="margin-top:12px"><li>Home</li><li>Take 1</li><li>Take 2</li><li>Take 3</li><li>BTS</li></ul>
  </div>
  <div class="abs" style="left:664px;top:2978px">
    <div class="col-title">OTHER LINKS</div>
    <ul class="col-list" style="margin-top:12px"><li>Terms &amp; conditions</li><li>Privacy Policy</li><li>Contact</li><li>FAQ</li></ul>
  </div>
  <div class="abs" style="left:843px;top:2978px;width:240px">
    <div class="col-title">CONTACT US</div>
    <div class="info" style="margin-top:14px"><svg width="12" height="14" viewBox="0 0 12 14"><path d="M6 0a5 5 0 0 1 5 5c0 4-5 9-5 9S1 9 1 5a5 5 0 0 1 5-5z" fill="#fff"/><circle cx="6" cy="5" r="2" fill="#222"/></svg><span>123 Lorem ipsum dolor sit amet,<br>consectetur adipiscing</span></div>
    <div class="info" style="margin-top:12px"><svg width="12" height="10" viewBox="0 0 12 10"><rect width="12" height="10" fill="#fff"/><path d="M0 0l6 5 6-5" stroke="#222" fill="none"/></svg><span>hello@plumfernstudio.com</span></div>
    <div class="info" style="margin-top:20px"><svg width="12" height="12" viewBox="0 0 12 12"><path d="M2 0l3 3-1.5 2a8 8 0 0 0 3.5 3.5L9 7l3 3-2 2C5 12 0 7 0 2z" fill="#fff"/></svg><span>555-014-2290</span></div>
  </div>

  <div class="abs footer-rule"></div>
  <div class="abs copyright">© 2023 Plumfern Studio &nbsp;&nbsp;&nbsp;&nbsp;|&nbsp;&nbsp;&nbsp;&nbsp; All rights reserved.</div>
</footer>

</body>
</html>
```